New business card design needed for Trucking/Staffing company!

I am looking for a business card design. The business name is Harbor Lane Freightworks, LLC. This company is a staffing company for commercial drivers/truck drivers. Most of our customers are trucking/supply companies. Our colors are blue/black/white/grey. The info I have on my current business cards is
-Spot for a name
-2 lines for an address
-3 lines for Office, cell, and fax
-email
-website(currently on backside of card with logo but can go anywhere)
Updates

Project Deadline Extended
Reason: Open to more designs

Target Market(s)

Trucking companies, building supply companies

Industry/Entity Type

Business

Contact Information for Business Card

Edgy but professional

Font styles to use
Other font styles liked:
• Open to suggestions

Colors
0555a3
000000
ffffff
9d9d9d

Requirements
Must have
• Must have the logo incorporated

```html
<!DOCTYPE html>
<html lang="en">
<head>
<meta charset="utf-8">
<title>Harbor Lane Freightworks – Business Card</title>
<link href="https://fonts.googleapis.com/css2?family=Montserrat:wght@400;500;700&display=swap" rel="stylesheet">
<style>
  :root {
    --page: #e8e6e3;
    --card: #000000;
    --ink: #ffffff;
    --accent: #2e3192;
    --accent-soft: #3d41a8;
    --muted: #9d9d9d;
  }
  * { box-sizing: border-box; margin: 0; padding: 0; }
  html, body { width: 1200px; height: 1000px; overflow: hidden; }
  body {
    background: var(--page);
    font-family: "Montserrat", Arial, sans-serif;
    color: var(--ink);
    position: relative;
  }
  .card {
    position: absolute;
    left: 265px;
    width: 665px;
    height: 397px;
    background: var(--card);
    border-radius: 24px;
    overflow: hidden;
  }
  .card--front { top: 73px; }
  .card--back { top: 533px; }

  .holder { position: absolute; left: 33px; top: 52px; }
  .holder__name { font-size: 21px; font-weight: 700; letter-spacing: .2px; }
  .holder__role { font-size: 15px; font-weight: 500; color: var(--accent-soft); margin-top: 3px; }

  .contacts { position: absolute; left: 33px; top: 139px; list-style: none; }
  .contacts li { display: flex; align-items: center; height: 23.6px; font-size: 15.5px; }
  .contacts svg { width: 14px; height: 14px; margin-right: 9px; fill: var(--muted); }

  .address { position: absolute; left: 33px; top: 272px; font-size: 15.5px; line-height: 22px; }
  .address__company { color: var(--accent-soft); font-weight: 700; margin-bottom: 1px; }

  .band { position: absolute; left: 0; bottom: 0; width: 320px; height: 32px; }
  .band path { fill: var(--accent); }

  .wordmark {
    position: absolute;
    color: var(--accent-soft);
    font-weight: 700;
    text-transform: uppercase;
    line-height: 1.1;
    text-align: right;
  }
  .card--front .wordmark { right: 32px; top: 170px; font-size: 27px; }
  .card--back .wordmark { left: 0; right: 0; top: 160px; font-size: 38px; text-align: center; }
</style>
</head>
<body>

<section class="card card--front">
  <div class="holder">
    <p class="holder__name">Daniel Foster</p>
    <p class="holder__role">Owner / Founder</p>
  </div>

  <ul class="contacts">
    <li><svg viewBox="0 0 14 14"><rect x="4" y="0" width="6" height="14" rx="1"/></svg>+ 999 999 999</li>
    <li><svg viewBox="0 0 14 14"><path d="M1 5 Q7 0 13 5 L11 7 L9 5 L5 5 L3 7Z M3 8 H11 V13 H3Z"/></svg>+ 999 999 999</li>
    <li><svg viewBox="0 0 14 14"><path d="M3 0 H11 V4 H3Z M0 5 H14 V11 H11 V9 H3 V11 H0Z M4 10 H10 V14 H4Z"/></svg>+ 999 999 999</li>
    <li><svg viewBox="0 0 14 14"><path d="M0 3 H14 V4 L7 8 L0 4Z M0 5.5 L7 9.5 L14 5.5 V11 H0Z"/></svg>info@harborlanefreight.com</li>
    <li><svg viewBox="0 0 14 14"><circle cx="7" cy="7" r="6.5"/></svg>www.harborlanefreight.com</li>
  </ul>

  <div class="address">
    <p class="address__company">Harbor Lane Freightworks</p>
    <p>48 Kestrel Way, Thornbury</p>
    <p>Gloucester GL12 7QT</p>
  </div>

  <svg class="band" viewBox="0 0 320 32" preserveAspectRatio="none" aria-hidden="true">
    <path d="M0 0 H280 Q310 0 320 32 H0Z"/>
  </svg>

  <p class="wordmark">Harbor Lane<br>Freightworks</p>
</section>

<section class="card card--back">
  <p class="wordmark">Harbor Lane Freightworks</p>
</section>

</body>
</html>
```